Wordpress Design Project - Executive Mentor Nexus

Website Brief

We are looking to have a design produced for a modern professional website. A mind map of the site can be found here: http://www.plotvine.example/view.htm?m=48120573b331498c97f2a1d6c0bb7f30

Each of the green tabs are pages just next to them is a very small green globe. If you click this. It will take you through to an example page for that section.

Task description
The website will be made up of:
1. A homepage (this will be the blog see http://www.tessawinbury.example for an example of the crisp and cleanness we are looking for)
2. A page that will have just a video and option page (see: http://qvlnacademy.example/ for example)
3. 3 pages all with the same structure. (see: http://qvlnacademy.example/zp27gkt93wqe/ for an example). Each will have:
a. A video
b. Tabs at the top of the video that link to the 3 videos and the sales page
c. Link to a resource download
d. Friendlane Comments section
4. 2 Page with about the experts and about our company (same style for both)
5. A page that will have a long well designed sales page (see: http://qvlnacademy.example/early-enrollment-2013/ for an example)
6. A page with testimonials on it (see http://www.tessawinbury.example/praise/)
7. A page that will describe the products, services and provision we will be offering
8. A page that will detail our involvement with charities and not for profits

Must Have
Edgey, crisp design, similar to Tessa Winburys. We would like the colours to match very well throughout the site and have a unique font (possibly manksans). We want it to have very clean integrations between copy and images with shadows on videos for example like with Tessawinburys page. We really love this design and would like this to be the inspiration for our site however it would need to certainly have a more executive feel to suit our target market.

We like the idea of some kind of circles, crisp clean lines, nice white space, simple design, corporate looking, communicates wealth/success/massive value. Based on the two logos of GTPLA and the Hub (see attached)

Target Market:
The target market includes intelligent, productive coaches, who are self employed or part of small firms. They are well educated, well read, socially conscious, and committed to making a profound difference with their clients...skilled at the actions of coaching, but not the business side. There will be a ratio of approximately 60% male / 40% female (really? The coaching industry is predominantly female, no?), with an age range of 40 to 60 years. English is our core language. Most will have secondary education and the salary range will be $90,000 to $400,000. We will have a global audience reach, although the primary markets will be North America, Europe and Australia/NZ.

Marketing Objective:
EMN will be an on-line resource for Executive Coaches. The intent of the design will be to present EMN to the world as a highly professional organization. The intent is not to characterize EMN as solely corporate, but will also incorporate elements of entrepreneurialism. We require the brand to incorporate these values:
• Trustworthy – you can trust us
• Professional – we are true professionals whose mission is to provide value to our clients
• Caring - Interested in our clients wellbeing – we are keenly interested in helping our clients build their knowledge, skills, and attitudes to be highly productive and successful
• Successful
• Knowledgeable – we have breadth and depth of knowledge in leadership
• World-class – we have a world-wide target market and, as such, need the brand to reflect a powerful and inclusive image
• Positive Energy - I would like the brand to have positive energy and very clean feng shui
• Prestige
• Massive Value
• Accessible
• Worldly/ Sophisticated
• Affordable
• Mission-critical

Details about the needs, wants, aspirations etc. of our target market
Executive coaches need a process and a system for creating opportunities to do the work they love with clients who are qualified to engage them and pay them. There is a scarcity mentality around their own finances, but ironically an abundance mentality for what's possible in the world and for their clients. They want to make a difference, they want to facilitate transformation, they want to be of deep service.

They aspire to make a decent living doing it! They need help bridging the gap between practitioner/service provider and financially successful entrepreneur/business owner/ leader. They also aspire to have it be easy, as it feels hard for them to generate the revenues they want to generate solely through coaching, so many turn to training, speaking, and other revenue streams.

Required assets to send through to web designer
1. Three blog posts. Each will have:
a. A video/audio
b. Summary of the points raised
c. Download (possibly slides)
2. A page that will have just a video and option page
a. Headline
b. Video
c. One paragraph summary of what we do
3. 3 launch videos. Here for each we will need
a. A video scripted and produced
b. Title for each
c. A resource download
4. Sales page
a. Video
b. Copy
i. Overview
ii. Content of course
iii. Guarentee
iv. Details of bonuses
v. Details of support
vi. Pricing broken down ($30,000 value = $2000)
c. Animated Gif
5. About the company and experts
a. Description of our company, it's vision, mission, purpose and core values.
b. Description of each of us,
i. our key facts and wows,
ii. a picture of us
iii. some interesting facts (giving personality)
iv. Lower down we will add in "Faculty" these will be any thought leaders we invite in to be part of the value delivery (will add to our credibility having such a strong team behind the project)
6. Testimonials
a. Testimonials from coaches from working with us
7. Products, services and provision we will be offering
a. A simple description of each of the key products/services we will be offering
i. Executive Mentor Sales
ii. Executive Mentor Marketing
iii. Executive Mentor Help
iv. Executive Mentor Mastermind
v. Executive Mentor Resources
a. List of the various charity work each of us have been involved with

Requirements
Must have
• Edgey, crisp design, similar to Tessa Winburys. We would like the colours to match very well throughout the site and have a unique font (possibly manksans). We want it to have very clean integrations between copy and images with shadows on videos for example like with Tessawinburys page. We really love this design and would like this to be the inspiration for our site however it would need to certainly have a more executive feel to suit our target market.

```html
<!DOCTYPE html>
<html lang="en">
<head>
<meta charset="utf-8">
<title>Executive Mentor Nexus</title>
<link href="https://fonts.googleapis.com/css2?family=Open+Sans:wght@400;600;700&family=PT+Serif&display=swap" rel="stylesheet">
<style>
:root{
  --orange:#e5662e;
  --orange-dark:#c9501d;
  --yellow:#f3b94b;
  --dark:#3b3b3b;
  --text:#6a6a6a;
  --muted:#8c8c8c;
  --line:#e4e4e4;
  --fb:#7b8fbe;
  --white:#ffffff;
}
*{box-sizing:border-box;margin:0;padding:0}
html,body{width:718px;height:1200px;overflow:hidden}
body{position:relative;background:var(--white);font-family:"Open Sans",Arial,sans-serif;color:var(--text)}
.abs{position:absolute}

.topbar{left:0;top:0;width:718px;height:6px;background:var(--dark)}
.header{left:0;top:6px;width:718px;height:110px;background:linear-gradient(#fafafa,#fff)}
.brand{left:55px;top:40px;font-size:15px;font-weight:600;color:var(--dark);letter-spacing:.2px;white-space:nowrap}
.search{left:558px;top:22px;width:106px;height:19px;border:1px solid #d6d6d6;border-radius:2px;background:#fff;box-shadow:inset 0 1px 2px rgba(0,0,0,.08);font-size:7px;font-style:italic;color:#aaa;padding:4px 0 0 10px}
.search svg{position:absolute;right:8px;top:5px}
.nav{top:75px;left:0;font-size:8.4px;color:#555}
.nav a{position:absolute;top:0;height:18px;line-height:18px;color:#555;text-decoration:none;white-space:nowrap}
.nav a.active{background:var(--orange);color:#fff;border-radius:3px;padding:0 11px}

.band{left:0;top:116px;width:718px;height:192px;background:var(--dark)}
.slider{left:54px;top:110px;width:612px;height:204px;background:#fff;border:1px solid #d8d8d8;box-shadow:0 10px 14px -6px rgba(0,0,0,.25)}
.slide{left:5px;top:5px;width:601px;height:192px;background:linear-gradient(100deg,#d4deea 0%,#8ea6c4 35%,#2c3c5a 60%,#c9d1dc 85%,#eef1f5 100%)}
.arrow{top:84px;width:14px;height:22px;background:rgba(255,255,255,.55)}
.arrow.next{background:rgba(60,60,60,.6)}

.welcome-title{left:55px;top:350px;font-size:14px;color:var(--orange);font-weight:400}
.welcome-copy{left:55px;top:375px;width:424px;font-size:7.5px;line-height:13.6px;color:var(--text)}
.btn-download{left:62px;top:437px;width:126px;height:22px;border-radius:12px;background:linear-gradient(#ef7a44,var(--orange-dark));box-shadow:0 0 0 2px #f3d3c3,0 2px 3px rgba(0,0,0,.25);color:#fff;font-size:9.4px;font-weight:600;padding:4px 0 0 12px}
.btn-download span{position:absolute;right:6px;top:5px;width:12px;height:12px;border-radius:50%;background:#fff}
.video{left:490px;top:356px;width:170px;height:96px;background:#1e1e1e;border:2px solid #111}
.video .frame{left:4px;top:4px;width:158px;height:76px;background:linear-gradient(90deg,#555,#888 40%,#444 70%,#777)}
.video .play{left:73px;top:35px;width:16px;height:11px;background:#111;border-radius:2px}
.video .bar{left:0;top:82px;width:166px;height:10px;background:#0b0b0b}
.video .progress{left:0;top:82px;width:166px;height:2px;background:#444}
.video .progress i{position:absolute;left:0;top:0;width:40px;height:2px;background:#d11}

.post{left:58px;width:418px;height:200px;background:#fff;border:1px solid var(--line);box-shadow:0 0 4px rgba(0,0,0,.06)}
.post-meta{position:absolute;left:13px;top:13px;font-size:6.6px;color:var(--muted);white-space:nowrap}
.post-meta b{font-weight:400;margin:0 6px;color:#aaa}
.post-ribbon{position:absolute;left:-5px;top:27px;width:418px;height:27px;background:var(--yellow);clip-path:polygon(0 0,100% 0,97% 100%,0 100%);font-size:11.2px;font-weight:400;color:#3a3a3a;padding:5px 0 0 16px}
.post-fold{position:absolute;left:-5px;top:54px;width:0;height:0;border-top:4px solid #b9862c;border-left:4px solid transparent}
.post-photo{position:absolute;left:12px;top:66px;width:148px;height:82px;box-shadow:0 1px 3px rgba(0,0,0,.3)}
.post-text{position:absolute;left:168px;top:62px;width:240px;font-size:7.3px;line-height:12.5px;text-align:justify;color:var(--text)}
.post-rule{position:absolute;left:12px;top:160px;width:396px;height:1px;background:var(--line)}
.post-actions{position:absolute;left:12px;top:174px;width:396px;height:12px;font-family:"PT Serif",Georgia,serif;font-size:7.2px;color:#666}
.post-actions .act{position:absolute;top:0;display:flex;align-items:center;gap:4px;white-space:nowrap}
.counter{position:absolute;top:0;height:10px;font-family:Arial,sans-serif;font-size:5.6px;line-height:10px;display:flex;gap:2px}
.counter .pill{padding:0 3px;border-radius:2px;color:#fff}
.counter .num{padding:0 3px;border:1px solid #ccc;border-radius:2px;color:#555;background:#fff;line-height:8px}

.pager{left:254px;top:1110px;height:14px;font-size:6.6px;color:#666;display:flex;align-items:center;gap:3px}
.pager .pg{width:13px;height:13px;border-radius:3px;background:#d4d4d4;color:#fff;font-size:6px;text-align:center;line-height:13px}
.pager .pg.on{background:#8a8a8a}
.pager .dots{width:10px;text-align:center}

.fb{left:493px;top:483px;width:166px;height:133px;background:#fff}
.fb-head{left:0;top:0;width:166px;height:24px;background:var(--fb);color:#fff;font-size:10px;font-weight:700;padding:4px 0 0 10px}
.fb-head span{font-weight:400}
.fb-count{left:0;top:36px;font-size:5.4px;color:#666}
.fb-like{left:118px;top:33px;width:46px;height:11px;border:1px solid #ccd;border-radius:2px;background:#eef1f7;font-size:5.4px;color:#3b5998;padding:1px 0 0 4px}
.fan{width:26px;height:27px;border:1px solid #ddd}
.fan-name{width:34px;text-align:center;font-size:4.6px;color:#777}

.contact{left:495px;top:636px;width:164px;height:206px;background:#efefef;border-radius:3px}
.contact-head{left:0;top:0;width:164px;height:28px;background:linear-gradient(#ef7a44,var(--orange-dark));color:#fff;font-size:11.5px;padding:6px 0 0 40px;border-radius:3px 3px 0 0}
.contact-head .icon{position:absolute;left:10px;top:4px;width:20px;height:20px;border-radius:50%;background:#fff}
.field{left:11px;width:140px;height:19px;background:#fff;border:1px solid #cfcfcf;font-size:7px;font-style:italic;color:#999;padding:4px 0 0 11px}
.submit{left:95px;top:178px;width:56px;height:20px;border-radius:10px;background:linear-gradient(#7a7a7a,#4a4a4a);color:#fff;font-size:8.6px;font-style:italic;text-align:center;line-height:20px}

.testi-head{left:502px;top:858px;font-size:11.4px;color:var(--orange);display:flex;align-items:center;gap:9px}
.testi-box{left:494px;top:878px;width:164px;height:110px;background:#fff;border:1px solid #ececec;box-shadow:0 1px 3px rgba(0,0,0,.08)}
.testi-text{left:12px;top:12px;width:140px;font-size:7px;line-height:13.6px;text-align:justify;color:var(--text)}
.testi-tail{left:631px;top:988px;width:0;height:0;border-top:10px solid #e8e8e8;border-left:14px solid transparent}
.testi-name{left:540px;top:995px;font-size:7.6px;color:var(--orange)}

.footer{left:0;top:1146px;width:718px;height:54px;background:var(--dark)}
.footer-links{left:60px;top:13px;font-size:7.4px;color:#ddd;white-space:nowrap}
.footer-links b{font-weight:400;margin:0 6px;color:#999}
.copyright{left:60px;top:33px;font-size:7.2px;color:#ccc;white-space:nowrap}
.social{top:20px;width:16px;height:16px;border-radius:50%;background:#6e6e6e;border:1px solid #888}
</style>
</head>
<body>

<div class="abs topbar"></div>
<header class="abs header">
  <div class="abs brand">Executive Mentor Nexus</div>
  <div class="abs search">Search
    <svg width="7" height="7" viewBox="0 0 7 7"><circle cx="3" cy="3" r="2.2" fill="none" stroke="#aaa" stroke-width=".8"/><line x1="4.6" y1="4.6" x2="6.5" y2="6.5" stroke="#aaa" stroke-width=".8"/></svg>
  </div>
  <nav class="abs nav">
    <a class="active" href="#" style="left:302px">HOME</a>
    <a href="#" style="left:369px">ABOUT</a>
    <a href="#" style="left:429px">WORK WITH US</a>
    <a href="#" style="left:522px">TESTIMONIALS</a>
    <a href="#" style="left:613px">CONTACT</a>
  </nav>
</header>

<div class="abs band"></div>
<section class="abs slider">
  <div class="abs slide" role="img" aria-label="Photo of business people in suits signing documents at a meeting table"></div>
  <div class="abs arrow" style="left:5px"><svg width="14" height="22"><polyline points="9,7 5,11 9,15" fill="none" stroke="#999" stroke-width="1"/></svg></div>
  <div class="abs arrow next" style="right:5px"><svg width="14" height="22"><polyline points="5,7 9,11 5,15" fill="none" stroke="#fff" stroke-width="1.4"/></svg></div>
</section>

<h1 class="abs welcome-title">Welcome to our site</h1>
<p class="abs welcome-copy">Sed ut perspiciatis unde omnis iste natus error sit voluptatem accusantium doloremque laudantium, totam rem aperiam, eaque ipsa quae ab illo inventore veritatis et quasi architecto beatae vitae dicta sunt explicabo. Nemo enim ipsam voluptatem quia voluptas sit aspernatur aut odit aut fugit, sed quia consequuntur magni dolores eos qui ratione voluptatem sequi nesciunt. Neque porro quisquam est, qui dolorem ipsum quia dolor sit amet, consectetur.</p>
<div class="abs btn-download">Resource download
  <span><svg width="12" height="12"><polyline points="5,3.5 8,6 5,8.5" fill="none" stroke="#c9501d" stroke-width="1.4"/></svg></span>
</div>

<div class="abs video">
  <div class="abs frame" role="img" aria-label="Video still of an audience seated in a conference room"></div>
  <div class="abs play"><svg width="16" height="11"><polygon points="6,3 11,5.5 6,8" fill="#fff"/></svg></div>
  <div class="abs bar"></div>
  <div class="abs progress"><i></i></div>
</div>

<article class="abs post" style="top:484px">
  <div class="post-meta">17 Hours Ago<b>|</b>39 Comments<b>|</b>28 Likes</div>
  <h2 class="post-ribbon">Nullam consequat lectus sit amet</h2>
  <div class="post-fold"></div>
  <div class="post-photo" role="img" aria-label="Photo of a presenter at a whiteboard speaking to an audience" style="background:linear-gradient(135deg,#e9ecef,#b7bcc2 55%,#4a3a32)"></div>
  <p class="post-text">Curabitur quis nisi quam. Etiam sit amet purus quis nisl vestibulum aliquet. Morbi viverra, massa nec convallis viverra, nisl augue aliquet nunc, sed ultrices augue turpis id diam. Cum sociis natoque penatibus et magnis dis parturient montes, nascetur ridiculus mus. Nam laoreet, nisl elementum sagittis venenatis, magna turpis pellentesque enim, et blandit elit nunc non augue.</p>
  <div class="post-rule"></div>
  <div class="post-actions">
    <span class="act" style="left:0">&#9744; Like</span>
    <span class="act" style="left:48px">&#9635; Share</span>
    <span class="act" style="left:96px">&#9673; Comment</span>
    <span class="act" style="left:163px">&#8599; Fix it!</span>
    <span class="counter" style="left:220px"><span class="pill" style="background:#5f7fbf">Like</span><span class="num">3k</span></span>
    <span class="counter" style="left:262px"><span class="pill" style="background:#4aa3d8">Post</span><span class="num">316</span></span>
    <span class="counter" style="left:310px"><span class="pill" style="background:#d9534f">+1</span><span class="num">81</span></span>
    <span class="counter" style="left:350px"><span class="pill" style="background:#e8583a">Share</span><span class="num">4.6K</span></span>
  </div>
</article>

<article class="abs post" style="top:692px">
  <div class="post-meta">17 Hours Ago<b>|</b>39 Comments<b>|</b>28 Likes</div>
  <h2 class="post-ribbon">Nullam consequat lectus sit amet</h2>
  <div class="post-fold"></div>
  <div class="post-photo" role="img" aria-label="Photo of a coach presenting a chart to a seated team" style="background:linear-gradient(135deg,#f4f5f7,#c9ccd2 50%,#2b2f3a)"></div>
  <p class="post-text">Curabitur quis nisi quam. Etiam sit amet purus quis nisl vestibulum aliquet. Morbi viverra, massa nec convallis viverra, nisl augue aliquet nunc, sed ultrices augue turpis id diam. Cum sociis natoque penatibus et magnis dis parturient montes, nascetur ridiculus mus. Nam laoreet, nisl elementum sagittis venenatis, magna turpis pellentesque enim, et blandit elit nunc non augue.</p>
  <div class="post-rule"></div>
  <div class="post-actions">
    <span class="act" style="left:0">&#9744; Like</span>
    <span class="act" style="left:48px">&#9635; Share</span>
    <span class="act" style="left:96px">&#9673; Comment</span>
    <span class="act" style="left:163px">&#8599; Fix it!</span>
    <span class="counter" style="left:220px"><span class="pill" style="background:#5f7fbf">Like</span><span class="num">3k</span></span>
    <span class="counter" style="left:262px"><span class="pill" style="background:#4aa3d8">Post</span><span class="num">316</span></span>
    <span class="counter" style="left:310px"><span class="pill" style="background:#d9534f">+1</span><span class="num">81</span></span>
    <span class="counter" style="left:350px"><span class="pill" style="background:#e8583a">Share</span><span class="num">4.6K</span></span>
  </div>
</article>

<article class="abs post" style="top:899px">
  <div class="post-meta">17 Hours Ago<b>|</b>39 Comments<b>|</b>28 Likes</div>
  <h2 class="post-ribbon">Nullam consequat lectus sit amet</h2>
  <div class="post-fold"></div>
  <div class="post-photo" role="img" aria-label="Photo of two businesswomen working at a laptop in a bright office" style="background:linear-gradient(135deg,#f2f3f5,#d8d2c8 50%,#9a8a78)"></div>
  <p class="post-text">Curabitur quis nisi quam. Etiam sit amet purus quis nisl vestibulum aliquet. Morbi viverra, massa nec convallis viverra, nisl augue aliquet nunc, sed ultrices augue turpis id diam. Cum sociis natoque penatibus et magnis dis parturient montes, nascetur ridiculus mus. Nam laoreet, nisl elementum sagittis venenatis, magna turpis pellentesque enim, et blandit elit nunc non augue.</p>
  <div class="post-rule"></div>
  <div class="post-actions">
    <span class="act" style="left:0">&#9744; Like</span>
    <span class="act" style="left:48px">&#9635; Share</span>
    <span class="act" style="left:96px">&#9673; Comment</span>
    <span class="act" style="left:163px">&#8599; Fix it!</span>
    <span class="counter" style="left:220px"><span class="pill" style="background:#5f7fbf">Like</span><span class="num">3k</span></span>
    <span class="counter" style="left:262px"><span class="pill" style="background:#4aa3d8">Post</span><span class="num">316</span></span>
    <span class="counter" style="left:310px"><span class="pill" style="background:#d9534f">+1</span><span class="num">81</span></span>
    <span class="counter" style="left:350px"><span class="pill" style="background:#e8583a">Share</span><span class="num">4.6K</span></span>
  </div>
</article>

<div class="abs pager">
  <span style="margin-right:2px">Page 1 of 32</span>
  <span class="pg on">1</span><span class="pg">2</span><span class="pg">3</span><span class="pg">4</span><span class="pg">5</span><span class="pg">6</span><span class="pg">7</span><span class="pg">8</span><span class="pg">&raquo;</span><span class="dots">...</span><span class="pg">&raquo;&raquo;</span>
</div>

<aside class="abs fb">
  <div class="abs fb-head">Connect <span>with</span> Friendlane</div>
  <div class="abs fb-count">347 people like</div>
  <div class="abs fb-like">Like</div>
  <div class="abs fan" style="left:2px;top:52px;background:#7a8fa8" role="img" aria-label="Member avatar"></div>
  <div class="abs fan" style="left:36px;top:52px;background:#4c8ea6" role="img" aria-label="Member avatar"></div>
  <div class="abs fan" style="left:71px;top:52px;background:#6b7a55" role="img" aria-label="Member avatar"></div>
  <div class="abs fan" style="left:105px;top:52px;background:#f2eeee" role="img" aria-label="Member avatar"></div>
  <div class="abs fan" style="left:140px;top:52px;background:#e6eec2" role="img" aria-label="Member avatar"></div>
  <div class="abs fan-name" style="left:-2px;top:81px">Nadia</div>
  <div class="abs fan-name" style="left:32px;top:81px">Stefano</div>
  <div class="abs fan-name" style="left:67px;top:81px">Sorin</div>
  <div class="abs fan-name" style="left:101px;top:81px">Mateo</div>
  <div class="abs fan-name" style="left:136px;top:81px">Maya</div>
  <div class="abs fan" style="left:2px;top:93px;background:#3a3a3a" role="img" aria-label="Member avatar"></div>
  <div class="abs fan" style="left:36px;top:93px;background:#8a8f96" role="img" aria-label="Member avatar"></div>
  <div class="abs fan" style="left:71px;top:93px;background:#f0f0f0" role="img" aria-label="Member avatar"></div>
  <div class="abs fan" style="left:105px;top:93px;background:#9a9a9a" role="img" aria-label="Member avatar"></div>
  <div class="abs fan" style="left:140px;top:93px;background:#a99ab8" role="img" aria-label="Member avatar"></div>
  <div class="abs fan-name" style="left:-2px;top:122px">Karel</div>
  <div class="abs fan-name" style="left:32px;top:122px">Kamal</div>
  <div class="abs fan-name" style="left:67px;top:122px">Manon</div>
  <div class="abs fan-name" style="left:101px;top:122px">Samir</div>
  <div class="abs fan-name" style="left:136px;top:122px">Malik</div>
</aside>

<section class="abs contact">
  <div class="abs contact-head"><span class="icon"><svg width="20" height="20" viewBox="0 0 20 20"><path d="M6 5c1-1 2 0 2.5 1.5S8 8 8 9s2 3 3 3 1.2-.5 2.5-.5S16 13 15 14s-3 1.5-6-1.5S5 6 6 5z" fill="#3d6fb0"/></svg></span>Contact us</div>
  <div class="abs field" style="top:42px">Name</div>
  <div class="abs field" style="top:67px">Email</div>
  <div class="abs field" style="top:93px">Phone</div>
  <div class="abs field" style="top:118px;height:51px">message</div>
  <div class="abs submit">SUBMIT</div>
</section>

<div class="abs testi-head">
  <svg width="20" height="14" viewBox="0 0 20 14"><path d="M2 2h14a2 2 0 0 1 2 2v5a2 2 0 0 1-2 2H8l-4 3v-3H2a2 2 0 0 1-2-2V4a2 2 0 0 1 2-2z" fill="#e2e2e2"/><text x="6" y="10" font-size="8" fill="#777" font-family="Georgia,serif">&ldquo;&rdquo;</text></svg>
  Testimonials
</div>
<div class="abs testi-box">
  <p class="abs testi-text">Nemo enim ipsam voluptatem quia voluptas sit aspernatur aut odit aut fugit, sed quia consequuntur magni dolores eos qui ratione voluptatem sequi nesciunt. Neque porro quisquam est, qui dolorem ipsum quia dolor sit amet,</p>
</div>
<div class="abs testi-tail"></div>
<div class="abs testi-name">Client Name, City</div>

<footer class="abs footer">
  <div class="abs footer-links">Home<b>|</b>About<b>|</b>Work with us<b>|</b>Testimonials<b>|</b>Contact</div>
  <div class="abs copyright">Copyright &copy; 2012&nbsp; www.executivementornexus.example &nbsp; All rights reserved.</div>
  <div class="abs social" style="left:581px"></div>
  <div class="abs social" style="left:602px"></div>
  <div class="abs social" style="left:623px"></div>
  <div class="abs social" style="left:644px"><svg width="14" height="14"><rect x="3.5" y="4.5" width="7" height="5" fill="none" stroke="#fff" stroke-width=".8"/><polyline points="3.5,4.5 7,7.5 10.5,4.5" fill="none" stroke="#fff" stroke-width=".8"/></svg></div>
</footer>

</body>
</html>
```